Makeup artist looking for business card design

- Business card to be memorable and recognisable

- I've attached photos of my logo (File 4), photos that I want to incorporate into the design (File 5,6 & 7) and an example of the design I like "Mirela Stott" (File 1)

- I've attached 3 photos of the designs I want to use, please use one of your choice

- Next to Instagram (File 2) and Facebook (File 3), please use their logo.

- No coloured background, either use the original background (grey) old white.

- Please include the following on the business card:
- Business name: LK Makeup Artistry
- My name: Rosalind Kerr
- Occupation: Makeup Artist
- Contact number: 0437 295 148
- Email: roskerr_makeup@mailvento.com
- Instagram (please use image): @lkmakeupartistry
- Facebook (please use image): www.pagelyne.com/LKMakeUpArtistry

Target Market(s)

Target woman for bridal makeup, occasion, fashion makeup and print.

Industry/Entity Type

Business

Requirements
Must have
• Logo provided and photo provided
Should not have
• Colourful background
Too cluttered
Shouldn't use old style font

```html
<!DOCTYPE html>
<html lang="en">
<head>
<meta charset="utf-8">
<title>LK Makeup Artistry – Business Card</title>
<link rel="stylesheet" href="https://fonts.googleapis.com/css2?family=Jost:wght@300;400&display=swap">
<style>
  :root {
    --backdrop: #bfbfbf;
    --card-white: #ffffff;
    --ink: #3a3a3a;
    --ink-soft: #4a4a4a;
    --rose: #c4809c;
    --skin-light: #f4d2cf;
    --skin-mid: #e7aeae;
    --skin-deep: #d98f94;
    --petal-light: #efe1f0;
    --petal-mid: #c7a3cf;
    --petal-deep: #8f6a9c;
    --mark-black: #111111;
  }
  * { box-sizing: border-box; margin: 0; padding: 0; }
  html, body {
    width: 1200px;
    height: 907px;
    overflow: hidden;
    background: var(--backdrop);
    font-family: "Jost", sans-serif;
  }
  .canvas {
    position: relative;
    width: 1200px;
    height: 907px;
    display: flex;
    align-items: center;
    justify-content: center;
    gap: 44px;
  }
  .card {
    position: relative;
    width: 530px;
    height: 324px;
    overflow: hidden;
    box-shadow: 0 6px 18px rgba(0,0,0,0.18);
  }

  /* Front */
  .card--front { background: var(--card-white); }
  .portrait {
    position: absolute;
    left: 0; top: 0;
    width: 200px;
    height: 100%;
    background: radial-gradient(ellipse at 55% 45%, var(--skin-light) 0%, var(--skin-mid) 60%, var(--skin-deep) 100%);
    border-radius: 0 70px 70px 0 / 0 50% 50% 0;
  }
  .identity {
    position: absolute;
    right: 34px;
    top: 38px;
    text-align: right;
  }
  .identity__name {
    font-weight: 400;
    font-size: 23px;
    letter-spacing: 2.5px;
    text-transform: uppercase;
    color: var(--ink);
  }
  .identity__role {
    font-weight: 300;
    font-size: 16px;
    color: var(--rose);
    margin-top: 2px;
  }
  .contacts {
    position: absolute;
    right: 34px;
    top: 138px;
    list-style: none;
    text-align: right;
    font-weight: 300;
    font-size: 16px;
    color: var(--ink-soft);
    line-height: 30px;
  }
  .contacts__item {
    display: flex;
    justify-content: flex-end;
    align-items: center;
    gap: 8px;
  }
  .contacts__icon {
    width: 14px;
    height: 14px;
    background: var(--ink-soft);
    border-radius: 2px;
  }
  .contacts__spacer { width: 14px; }

  /* Back */
  .card--back { background: var(--petal-mid); }
  .bloom {
    position: absolute;
    inset: 0;
    background:
      radial-gradient(ellipse at 32% 62%, var(--card-white) 0%, var(--petal-light) 22%, transparent 48%),
      radial-gradient(ellipse at 80% 20%, var(--petal-light) 0%, transparent 45%),
      linear-gradient(160deg, var(--petal-mid) 0%, var(--petal-deep) 100%);
  }
  .brand {
    position: absolute;
    right: 28px;
    top: 140px;
    display: flex;
    align-items: center;
    gap: 8px;
  }
  .brand__dot {
    width: 34px;
    height: 34px;
    border-radius: 50%;
    background: var(--mark-black);
  }
  .brand__name {
    font-weight: 300;
    font-size: 13px;
    letter-spacing: 1.5px;
    text-transform: uppercase;
    color: var(--mark-black);
  }
</style>
</head>
<body>
  <main class="canvas">
    <section class="card card--front">
      <div class="portrait" role="img" aria-label="Close-up beauty portrait showing lilac eye and lip makeup"></div>
      <header class="identity">
        <h1 class="identity__name">Rosalind Kerr</h1>
        <p class="identity__role">Makeup Artist</p>
      </header>
      <ul class="contacts">
        <li class="contacts__item"><span>0437 295 148</span><span class="contacts__spacer"></span></li>
        <li class="contacts__item"><span>roskerr_makeup@mailvento.com</span><span class="contacts__spacer"></span></li>
        <li class="contacts__item"><span>www.pagelyne.com/LKMakeUpArtistry</span><span class="contacts__icon"></span></li>
        <li class="contacts__item"><span>@lkmakeupartistry</span><span class="contacts__icon"></span></li>
      </ul>
    </section>

    <section class="card card--back">
      <div class="bloom" role="img" aria-label="Soft lilac and white flower petals close-up"></div>
      <div class="brand">
        <span class="brand__dot"></span>
        <span class="brand__name">LK Makeup Artistry</span>
      </div>
    </section>
  </main>
</body>
</html>
```